Industrial Design Business Card

I am an industrial designer that needs a nice business card that gives a sense of my personal brand (the work I do, how I'm different than others though subtle design). Since I am a designer, myself, the business card needs to have an impeccable design, while feeling like it represents me. Please see the link to my portfolio where you can get a better sense for me.

http://www.markdpelletier.example/

Target Market(s)

Potential employers, industrial designers

Industry/Entity Type

Business

Contact Information for Business Card

Mark Pelletier
Industrial Designer
markpelletierdesign.example
markpelletierdesign@mailbox.example
(555) 218-4370

Font styles to use
Sans Serif

Colors

Designer to choose colors to be used in the design.

Requirements
Must have
• Must have all of the business card details - ideally in that order. If it will look better in a different order, that's fine.
• Simple design - not too flashy. Using a font that is not a pre-set will likely be key to making this simple but also stand out. But also keep somewhat consistent with the fonts and look of my portfolio (markpelletierdesign.example).
• It needs to catch someone's attention while also being simple (not too flashy) design. That is the big challenge.
Should not have
• Random pictures off the internet.

```html
<!DOCTYPE html>
<html lang="en">
<head>
<meta charset="utf-8">
<title>Mark Pelletier — Business Card</title>
<link rel="stylesheet" href="https://fonts.googleapis.com/css2?family=Cinzel:wght@400;600&family=Lato:wght@400&display=swap">
<style>
  :root {
    --backdrop: #a6a6a6;
    --card: #ffffff;
    --band-dark: #2b2829;
    --band-grey: #6c696a;
    --ink: #231f20;
    --ink-soft: #5a5758;
    --name-grey: #9b999a;
    --faint: #ececec;
    --serif: "Cinzel", "Trajan Pro", serif;
    --sans: "Lato", "Helvetica Neue", Arial, sans-serif;
  }
  * { box-sizing: border-box; margin: 0; padding: 0; }
  html, body { width: 1200px; height: 900px; overflow: hidden; }
  body { background: var(--backdrop); position: relative; font-family: var(--sans); }

  .card {
    position: absolute; top: 306px; width: 440px; height: 271px;
    background: var(--card); border-radius: 12px; overflow: hidden;
    box-shadow: 2px 3px 5px rgba(0,0,0,0.35);
  }
  .card--front { left: 149px; }
  .card--back { left: 608px; }

  /* Front */
  .band { position: absolute; left: 0; top: 0; width: 100%; height: 97px; background: var(--band-dark); }
  .band__tail { position: absolute; left: 344px; top: 0; width: 96px; height: 97px; background: var(--band-grey); }
  .seal {
    position: absolute; left: 284px; top: 0; width: 120px; height: 120px;
    margin-top: -0px; top: 0px; transform: translateY(0);
    border-radius: 50%; background: var(--card);
    top: 0; left: 284px;
  }
  .seal { top: 0px; }
  .seal-wrap { position: absolute; left: 284px; top: 0px; width: 120px; height: 120px; top: 0; }
  .mark {
    position: absolute; border-radius: 50%; border: 2px solid var(--ink);
    display: flex; align-items: center; justify-content: center; text-align: center;
    font-family: var(--serif); color: var(--ink); line-height: 1.1;
  }
  .card--front .seal { top: 0; transform: translateY(0); }
  .band-name {
    position: absolute; left: 24px; top: 34px;
    font-family: var(--serif); font-size: 25px; letter-spacing: 0.5px; color: #fff; white-space: nowrap;
  }
  .band-name .surname, .holder .surname { color: var(--name-grey); }

  .holder { position: absolute; left: 21px; top: 138px; font-family: var(--serif); font-size: 17px; color: var(--ink); }
  .holder .surname { color: var(--ink-soft); }
  .role { position: absolute; left: 21px; top: 159px; font-size: 12.5px; color: var(--ink); }

  .contacts { position: absolute; left: 21px; top: 196px; list-style: none; font-size: 12.5px; color: var(--ink); }
  .contacts li { display: flex; align-items: center; gap: 3px; height: 16px; }
  .contacts svg { width: 14px; height: 14px; flex: none; }

  /* Back */
  .ghost-ring { position: absolute; left: 0; top: 0; }
  .back-name {
    position: absolute; left: 0; width: 100%; top: 152px; text-align: center;
    font-family: var(--serif); font-size: 31px; color: var(--ink); white-space: nowrap;
  }
  .back-name .surname { color: var(--ink-soft); }
  .back-url {
    position: absolute; left: 0; width: 100%; top: 217px; text-align: center;
    font-family: var(--serif); font-weight: 600; font-size: 12px; letter-spacing: 1.2px; color: var(--ink);
  }
</style>
</head>
<body>

<section class="card card--front" aria-label="Business card front">
  <div class="band"></div>
  <div class="band__tail"></div>
  <div class="band-name">Mark <span class="surname">Pelletier</span></div>
  <div class="seal" style="top:0;left:284px;transform:translateY(0);top:0;"></div>
  <div class="mark" style="left:306px;top:22px;width:78px;height:78px;font-size:9.5px;">Mark<br>Pelletier</div>

  <p class="holder">Mark <span class="surname">Pelletier</span></p>
  <p class="role">Industrial Designer</p>
  <ul class="contacts">
    <li>
      <svg viewBox="0 0 14 14"><circle cx="7" cy="7" r="6.2" fill="none" stroke="#231f20" stroke-width="1"/><path d="M4 8.3h6v1.3H4zM4.6 8.3l1-2.4h2.8l1 2.4zM3.6 6l1-1.4h4.8l1 1.4z" fill="#231f20"/></svg>
      (555) 218-4370
    </li>
    <li>
      <svg viewBox="0 0 14 14"><circle cx="7" cy="7" r="6.2" fill="none" stroke="#231f20" stroke-width="1"/><rect x="3.8" y="4.8" width="6.4" height="4.4" fill="#231f20"/><path d="M3.8 4.8L7 7.3l3.2-2.5" fill="none" stroke="#fff" stroke-width="0.7"/></svg>
      markpelletierdesign@mailbox.example
    </li>
    <li>
      <svg viewBox="0 0 14 14"><circle cx="7" cy="7" r="6.2" fill="none" stroke="#231f20" stroke-width="1"/><circle cx="7" cy="7" r="3.4" fill="#231f20"/><path d="M3.6 7h6.8M7 3.6v6.8" stroke="#fff" stroke-width="0.6"/></svg>
      www.markpelletierdesign.example
    </li>
  </ul>
</section>

<section class="card card--back" aria-label="Business card back">
  <svg class="ghost-ring" width="440" height="271" aria-hidden="true">
    <circle cx="150" cy="150" r="118" fill="none" stroke="var(--faint)" stroke-width="22"/>
  </svg>
  <div class="mark" style="left:177px;top:66px;width:82px;height:82px;font-size:10px;background:#fff;">Mark<br>Pelletier</div>
  <div class="back-name">Mark <span class="surname">Pelletier</span></div>
  <div class="back-url">www.markpelletierdesign.example</div>
</section>

</body>
</html>
```